Business Card for Orvane Parts Wholesale supplier

Hi There! I need a new business card for our company. We are specialized in selling Orvane parts, mostly we sell new LCD screens for Telvox and Slatrons. I would like to see that back in the design.

You can find the colors and logo's on our website: www.dorvak-example.nl

Industry/Entity Type

Business

Contact Information for Business Card

My Details:
Lars Vintorp

Phone: 0031612873406
E-mail: Lars@dorvak-example.nl

Slogan: "Because Quality Matters"

Font styles to use
Sans Serif

Colors

Designer to choose colors to be used in the design.

Requirements
Must have
• A Black backside with the Dorvak logo on it. The front side should be clean with only my contact details.
• But I'm also open for something really different or awesome!
Nice to have
• Remember that we are in the parts & repairing industry, So i'll be handing those business cards mainly to repair companies. Maybe you can do something with that thought :)

```html
<!DOCTYPE html>
<html lang="en">
<head>
<meta charset="utf-8">
<title>Dorvak Business Card</title>
<link rel="stylesheet" href="https://fonts.googleapis.com/css2?family=Open+Sans:wght@400;600;700&display=swap">
<style>
  :root {
    --backdrop: #5f676c;
    --card-white: #ffffff;
    --card-black: #050505;
    --ink: #1a1a1a;
    --accent: #f26a1b;
    --muted: #d9d9d9;
    --soft-white: #e6e6e6;
  }
  * { box-sizing: border-box; margin: 0; padding: 0; }
  html, body { width: 1200px; height: 900px; overflow: hidden; }
  body {
    background: var(--backdrop);
    font-family: "Open Sans", sans-serif;
    display: flex;
    flex-direction: column;
    align-items: center;
    justify-content: center;
    gap: 56px;
  }
  .card {
    position: relative;
    width: 620px;
    height: 354px;
    border-radius: 18px;
    overflow: hidden;
  }
  .card--front { background: var(--card-white); color: var(--ink); }
  .card--back {
    background: var(--card-black);
    display: flex;
    flex-direction: column;
    align-items: center;
    justify-content: center;
  }
  .wordmark {
    display: flex;
    align-items: center;
    gap: 10px;
    font-weight: 700;
    letter-spacing: 0.5px;
  }
  .wordmark__square {
    width: 24px;
    height: 24px;
    background: var(--accent);
  }
  .card--front .wordmark {
    position: absolute;
    left: 44px;
    top: 40px;
    font-size: 36px;
    color: var(--ink);
  }
  .holder-name {
    position: absolute;
    left: 44px;
    top: 140px;
    font-size: 22px;
    font-weight: 400;
    color: var(--accent);
  }
  .divider {
    position: absolute;
    left: 40px;
    right: 40px;
    top: 176px;
    height: 2px;
    background: var(--accent);
  }
  .contact-list {
    position: absolute;
    left: 44px;
    top: 188px;
    list-style: none;
    font-size: 14px;
    line-height: 24px;
  }
  .contact-list li { display: flex; align-items: center; gap: 10px; }
  .contact-list svg { width: 13px; height: 13px; fill: var(--accent); flex: none; }
  .tools-art {
    position: absolute;
    right: 54px;
    top: 44px;
    width: 130px;
    height: 110px;
    border-radius: 10px;
    background: linear-gradient(135deg, #eeeeee, #e2e2e2);
  }
  .slogan {
    position: absolute;
    right: 44px;
    top: 150px;
    font-size: 15px;
    font-weight: 400;
  }
  .industry {
    position: absolute;
    right: 44px;
    top: 186px;
    font-size: 15px;
    font-weight: 400;
  }
  .card--back .wordmark {
    font-size: 64px;
    color: #ffffff;
    gap: 16px;
  }
  .card--back .wordmark__square { width: 40px; height: 40px; }
  .back-url {
    margin-top: 26px;
    font-size: 15px;
    color: var(--soft-white);
  }
</style>
</head>
<body>
  <section class="card card--front" aria-label="Card front">
    <div class="wordmark"><span class="wordmark__square"></span>dorvak</div>
    <div class="tools-art" role="img" aria-label="Faint crossed wrench and screwdriver illustration"></div>
    <p class="holder-name">Lars Vintorp</p>
    <p class="slogan">Because Quality Matters</p>
    <div class="divider"></div>
    <p class="industry">Parts &amp; Repairing Industry</p>
    <ul class="contact-list">
      <li>
        <svg viewBox="0 0 24 24" aria-hidden="true"><path d="M6.6 10.8a15.1 15.1 0 0 0 6.6 6.6l2.2-2.2a1 1 0 0 1 1-.25 11.4 11.4 0 0 0 3.6.57 1 1 0 0 1 1 1V20a1 1 0 0 1-1 1A17 17 0 0 1 3 4a1 1 0 0 1 1-1h3.5a1 1 0 0 1 1 1c0 1.25.2 2.45.57 3.57a1 1 0 0 1-.25 1z"/></svg>
        0031612873406
      </li>
      <li>
        <svg viewBox="0 0 24 24" aria-hidden="true"><path d="M2 5h20v14H2z M3.5 6.5 12 13l8.5-6.5" fill="var(--accent)"/><path d="M3.5 6.5 12 13l8.5-6.5" fill="none" stroke="#fff" stroke-width="1.6"/></svg>
        Lars@dorvak-example.nl
      </li>
      <li>
        <svg viewBox="0 0 24 24" aria-hidden="true"><circle cx="12" cy="12" r="10"/><path d="M2 12h20M12 2c3 3 3 17 0 20M12 2c-3 3-3 17 0 20" fill="none" stroke="#fff" stroke-width="1.4"/></svg>
        www.dorvak-example.nl
      </li>
    </ul>
  </section>

  <section class="card card--back" aria-label="Card back">
    <div class="wordmark"><span class="wordmark__square"></span>dorvak</div>
    <p class="back-url">www.dorvak-example.nl</p>
  </section>
</body>
</html>
```